Business card design reauest

2 sided. White on both sides

Gordon Mabry

Song Lam, Vietnam

Cell Phone / Whatsapp/ Wechat/Zalo
1-555-382-7194
Gmabry@kwpartsworks.vn
Www.kwpartsworks.vn
Www.kwpartsworks.com

Industry/Entity Type

Sofa and furniture and kitchen

Contact Information for Business Card

2 sided. White on both sides Gordon Mabry Song Lam, Vietnam Cell Phone / Whatsapp/ Wechat/Zalo 1-555-382-7194 Gmabry@kwpartsworks.vn Www.kwpartsworks.vn Www.kwpartsworks.com

```html
<!DOCTYPE html>
<html lang="en">
<head>
<meta charset="utf-8">
<title>KW Parts Works – Business Card</title>
<link rel="stylesheet" href="https://fonts.googleapis.com/css2?family=Cinzel:wght@500&family=Poppins:wght@400&display=swap">
<style>
  :root {
    --backdrop: #cfc6b8;
    --card: #ffffff;
    --green: #169a46;
    --ink: #231f20;
    --shadow: rgba(0, 0, 0, 0.28);
  }
  * { box-sizing: border-box; margin: 0; padding: 0; }
  html, body {
    width: 1189px;
    height: 1200px;
    overflow: hidden;
    background: var(--backdrop);
  }
  .canvas {
    position: relative;
    width: 1189px;
    height: 1200px;
  }
  .card {
    position: absolute;
    left: 169px;
    width: 851px;
    height: 484px;
    background: var(--card);
    border-radius: 34px;
    box-shadow: 0 6px 14px var(--shadow);
  }
  .card--front { top: 112px; }
  .card--back { top: 641px; }

  .brand {
    position: absolute;
    display: flex;
    align-items: center;
    gap: 12px;
    font-family: "Cinzel", serif;
    font-weight: 500;
    color: var(--green);
    white-space: nowrap;
    transform: translate(-50%, -50%);
  }
  .brand__mark {
    width: 16px;
    height: 16px;
    background: var(--green);
  }
  .card--front .brand {
    left: 230px;
    top: 345px;
    font-size: 36px;
  }
  .card--back .brand {
    left: 50%;
    top: 243px;
    font-size: 41px;
  }

  .holder {
    position: absolute;
    left: 500px;
    top: 222px;
  }
  .holder__name {
    font-family: "Cinzel", serif;
    font-weight: 500;
    font-size: 27px;
    color: var(--green);
    letter-spacing: 0.3px;
    white-space: nowrap;
    line-height: 1.2;
  }
  .holder__rule {
    width: 122px;
    height: 3px;
    margin-top: 4px;
    background: var(--ink);
  }

  .contacts {
    position: absolute;
    left: 502px;
    top: 290px;
    list-style: none;
  }
  .contacts__item {
    display: flex;
    align-items: center;
    height: 31px;
    font-family: "Poppins", sans-serif;
    font-size: 20px;
    color: var(--ink);
    white-space: nowrap;
  }
  .contacts__icon {
    flex: none;
    width: 22px;
    height: 22px;
    margin-right: 9px;
  }
</style>
</head>
<body>
<main class="canvas">

  <section class="card card--front" aria-label="Business card front">
    <div class="brand">
      <span class="brand__mark"></span>
      <span class="brand__name">KW PARTS WORKS</span>
    </div>

    <div class="holder">
      <h1 class="holder__name">GORDON MABRY</h1>
      <div class="holder__rule"></div>
    </div>

    <ul class="contacts">
      <li class="contacts__item">
        <svg class="contacts__icon" viewBox="0 0 22 22" aria-hidden="true">
          <rect width="22" height="22" rx="2" fill="var(--green)"/>
          <rect x="7" y="4" width="8" height="14" rx="1.2" fill="none" stroke="#fff" stroke-width="1.8"/>
        </svg>
        1-555-382-7194
      </li>
      <li class="contacts__item">
        <svg class="contacts__icon" viewBox="0 0 22 22" aria-hidden="true">
          <rect width="22" height="22" rx="2" fill="var(--green)"/>
        </svg>
        gmabry@kwpartsworks.vn
      </li>
      <li class="contacts__item">
        <svg class="contacts__icon" viewBox="0 0 22 22" aria-hidden="true">
          <rect width="22" height="22" rx="2" fill="var(--green)"/>
        </svg>
        www.kwpartsworks.vn
      </li>
      <li class="contacts__item">
        <svg class="contacts__icon" viewBox="0 0 22 22" aria-hidden="true">
          <rect width="22" height="22" rx="2" fill="var(--green)"/>
        </svg>
        www.kwpartsworks.com
      </li>
      <li class="contacts__item">
        <svg class="contacts__icon" viewBox="0 0 22 22" aria-hidden="true">
          <rect width="22" height="22" rx="2" fill="var(--green)"/>
          <path d="M11 4.5a4.8 4.8 0 0 0-4.8 4.8c0 3.4 4.8 8.2 4.8 8.2s4.8-4.8 4.8-8.2A4.8 4.8 0 0 0 11 4.5z" fill="#fff"/>
          <circle cx="11" cy="9.3" r="1.8" fill="var(--green)"/>
        </svg>
        Song Lam, Vietnam
      </li>
    </ul>
  </section>

  <section class="card card--back" aria-label="Business card back">
    <div class="brand">
      <span class="brand__mark"></span>
      <span class="brand__name">KW PARTS WORKS</span>
    </div>
  </section>

</main>
</body>
</html>
```